serious, thorough, light and simple - that's my advice and mediations

My business card should combine my logo (uploaded file) and my homepage (https://fellor-mediation.webnestsite.com).

Contact Information for Business Card

Name: Sabine Fellor di Vanti
Phone: 076 412 58 94
mail: sfellor@postkiv.ch
web: www.fellor-di-vanti.ch

```html
<!DOCTYPE html>
<html lang="de">
<head>
<meta charset="utf-8">
<title>Business Card – Sabine Fellor di Vanti</title>
<link rel="stylesheet" href="https://fonts.googleapis.com/css2?family=Poppins:wght@400;500&display=swap">
<style>
  :root {
    --bg-top: #e4e4e4;
    --bg-bottom: #cfcfcf;
    --card: #ffffff;
    --gold: #b08a52;
    --green: #0a6b3f;
    --blue: #1e3f80;
    --ink-white: #ffffff;
  }
  html, body {
    margin: 0;
    padding: 0;
    overflow: hidden;
  }
  .canvas {
    width: 1200px;
    height: 961px;
    background: linear-gradient(180deg, var(--bg-top), var(--bg-bottom));
    position: relative;
    font-family: "Poppins", sans-serif;
  }
  .card {
    position: absolute;
    top: 309px;
    width: 530px;
    height: 343px;
    background: var(--card);
    box-shadow: 0 10px 28px rgba(0, 0, 0, 0.18);
  }
  .card--front { left: 45px; }
  .card--back { left: 625px; }
  .card svg { display: block; }
  .brand-name { fill: var(--gold); font-weight: 500; }
  .brand-dot { fill: var(--blue); }
  .divider { stroke: var(--green); stroke-width: 1.2; }
  .person-name { fill: var(--gold); font-size: 18px; font-weight: 400; }
  .person-role { fill: var(--green); font-size: 12.5px; font-weight: 400; }
  .contact-line { fill: var(--green); font-size: 13px; font-weight: 400; }
  .contact-icon { fill: var(--blue); }
  .contact-glyph { fill: none; stroke: var(--ink-white); stroke-width: 1.1; }
  .accent-line { fill: none; stroke: var(--gold); stroke-width: 4.5; }
  .web-address { fill: var(--ink-white); font-size: 13px; letter-spacing: 0.3px; }
</style>
</head>
<body>
<div class="canvas">

  <section class="card card--front" aria-label="Vorderseite">
    <svg width="530" height="343" viewBox="0 0 530 343">
      <defs>
        <linearGradient id="bandGradient" x1="0" y1="0" x2="1" y2="0">
          <stop offset="0" stop-color="#1e3f80"/>
          <stop offset="0.55" stop-color="#144f6a"/>
          <stop offset="1" stop-color="#08703c"/>
        </linearGradient>
        <path id="urlPath" d="M 40 222 C 130 248 210 290 262 336"/>
      </defs>

      <g class="brand">
        <circle class="brand-dot" cx="46" cy="82" r="9"/>
        <text class="brand-name" x="64" y="90" font-size="24">Klarweg Mediation</text>
      </g>

      <line class="divider" x1="282" y1="150" x2="282" y2="232"/>

      <g class="contact">
        <text class="person-name" x="300" y="168">Sabine Fellor di Vanti</text>
        <text class="person-role" x="300" y="186">Managing Director</text>

        <circle class="contact-icon" cx="307" cy="207" r="7"/>
        <rect class="contact-glyph" x="304.2" y="202.5" width="5.6" height="9" rx="1"/>
        <text class="contact-line" x="320" y="212">076 412 58 94</text>

        <circle class="contact-icon" cx="307" cy="228" r="7"/>
        <rect class="contact-glyph" x="302.8" y="225" width="8.4" height="6"/>
        <polyline class="contact-glyph" points="302.8,225 307,228.5 311.2,225"/>
        <text class="contact-line" x="320" y="233">sfellor@postkiv.ch</text>
      </g>

      <path class="wave-band" fill="url(#bandGradient)"
            d="M 0 198 C 120 218 230 262 300 343 L 0 343 Z"/>
      <path class="accent-line" d="M 0 158 C 150 182 290 240 360 343"/>

      <text class="web-address">
        <textPath href="#urlPath">www.fellor-di-vanti.ch</textPath>
      </text>
    </svg>
  </section>

  <section class="card card--back" aria-label="Rückseite">
    <svg width="530" height="343" viewBox="0 0 530 343">
      <g class="brand">
        <circle class="brand-dot" cx="148" cy="163" r="10"/>
        <text class="brand-name" x="168" y="172" font-size="26">Klarweg Mediation</text>
      </g>
    </svg>
  </section>

</div>
</body>
</html>
```